Create a memorable Web Design for real estate branding

we are a Minnepolis brokerage and boutique housing specialist with over 27 years of experience in the Global furnished housing industry, servicing the Greater Los Angeles area. Specializing in “warm environments” we offer a customized approach to satisfying our guests and client’s needs by offering a wide array of options in highly desirable areas. Additionally, Lanterly Homes Collective offers assistance and expertise to home buyers, sellers and investors.

Industry/Entity Type

Real Estate

Number of Pages Required

1 page

Font styles to use
Serif
Sans Serif
Decorative

```html
<!DOCTYPE html>
<html lang="en">
<head>
<meta charset="utf-8">
<title>Norvale Real Estate</title>
<link rel="stylesheet" href="https://fonts.googleapis.com/css2?family=Cinzel:wght@400;700&family=Open+Sans:wght@400;600;700&family=Montserrat:wght@700&display=swap">
<style>
:root{
  --teal:#0ea88e;
  --lime:#8cc63f;
  --black:#050505;
  --ink:#222;
  --muted:#555;
  --light:#f1f1f1;
  --line:#d8d8d8;
  --footer:#1c2229;
  --white:#fff;
}
*{box-sizing:border-box;margin:0;padding:0}
html,body{width:1200px;height:2808px;overflow:hidden}
body{font-family:'Open Sans',Arial,sans-serif;color:var(--ink);background:var(--white);position:relative}
.serif{font-family:'Cinzel',Georgia,serif}

.topbar{height:34px;background:var(--teal);color:var(--white);font-size:13px;display:flex;align-items:center;padding:0 80px;justify-content:space-between}
.topbar .contact{display:flex;gap:26px;align-items:center}
.topbar .contact span{display:flex;align-items:center;gap:8px}
.topbar .social{display:flex;gap:20px}
.topbar .social i{width:12px;height:12px;border-radius:50%;background:var(--white);display:block}

.header{height:131px;background:var(--black);position:relative}
.brand{position:absolute;left:79px;top:48px;font-family:'Cinzel',Georgia,serif;font-weight:700;font-size:34px;line-height:1.05;color:var(--teal);width:320px}
.brand small{display:block;font-size:24px;font-weight:700;letter-spacing:2px}
.cta{position:absolute;left:844px;top:22px;width:277px;height:47px;background:var(--lime);color:#111;font-family:'Cinzel',Georgia,serif;font-weight:700;font-size:16px;display:flex;align-items:center;justify-content:center;border:1px solid #6f9e2e}
.nav{position:absolute;left:446px;top:92px;display:flex;font-family:'Cinzel',Georgia,serif;font-size:15px;font-weight:700;color:var(--white)}
.nav a{color:inherit;text-decoration:none;padding:0 12px;border-left:1px solid #777;line-height:16px}
.nav a:first-child{border-left:0;padding-left:0;color:var(--lime)}

.hero{height:509px;position:relative;background:linear-gradient(180deg,#6c9fd8 0%,#9cc0e6 35%,#7d8795 62%,#6a6a5d 82%,#3f5b34 100%)}
.hero .arrow{position:absolute;top:400px;width:30px;height:30px;border-radius:50%;display:flex;align-items:center;justify-content:center}
.hero .prev{left:38px;background:var(--white)}
.hero .next{left:1135px;background:var(--lime)}
.hero .caption{position:absolute;left:0;right:0;bottom:0;height:51px;background:rgba(0,0,0,.55);color:var(--white);font-family:'Montserrat',Arial,sans-serif;font-weight:700;font-size:25px;display:flex;align-items:center;justify-content:center}

.welcome{height:664px;background:linear-gradient(135deg,#f4f4f4,#ebebeb 50%,#f6f6f6);text-align:center;position:relative}
.welcome h1{position:absolute;top:48px;left:0;right:0;font-family:'Cinzel',Georgia,serif;font-weight:400;font-size:32px;color:#111}
.welcome h1 b{color:var(--teal);font-weight:700;margin-left:10px}
.welcome .intro{position:absolute;left:94px;width:1012px;top:116px;font-size:14.5px;line-height:21px;color:#222}
.offer{position:absolute;top:223px;width:440px;text-align:center}
.offer.buy{left:130px}
.offer.sell{left:631px}
.offer .photo{width:396px;height:264px;margin:0 auto}
.offer.buy .photo{background:linear-gradient(180deg,#b8673a,#8a7a6c 40%,#c7b9a6)}
.offer.sell .photo{background:linear-gradient(180deg,#a9b8c9,#6a7f6a 60%,#3f6b34)}
.offer h3{font-weight:400;font-size:18px;margin:14px 0 8px;color:#111}
.offer p{font-size:14.5px;line-height:21px;color:#222}

.why{height:530px;position:relative;text-align:center}
.why h2{position:absolute;top:56px;left:0;right:0;font-family:'Cinzel',Georgia,serif;font-weight:700;font-size:27px;letter-spacing:1px}
.why h2::after{content:"";display:block;width:230px;height:1px;background:var(--line);margin:14px auto 0}
.feature{position:absolute;width:300px;text-align:center}
.feature .icon{width:97px;height:97px;border-radius:50%;border:2px solid #222;margin:0 auto;display:flex;align-items:center;justify-content:center}
.feature .icon.active{background:var(--teal);border-color:var(--teal)}
.feature p{margin-top:17px;font-size:18px;text-transform:uppercase;color:#222}

.panels{height:532px;background:var(--light);position:relative}
.panel{position:absolute;top:0;width:330px}
.panel h2{position:absolute;top:60px;font-family:'Cinzel',Georgia,serif;font-weight:400;font-size:23px;color:#111;width:318px;display:flex;justify-content:space-between}
.panel h2 span.nav-arrows{font-family:'Open Sans',sans-serif;font-size:20px;color:#777}
.panel .rule{position:absolute;top:105px;left:0;width:318px;height:2px;background:linear-gradient(90deg,#ccc,transparent)}
.card{position:absolute;top:120px;height:352px;width:328px;background:var(--white);box-shadow:0 1px 5px rgba(0,0,0,.35)}
.listing .photo{margin:10px;height:158px;background:linear-gradient(180deg,#5d8fd6,#a9c1df 45%,#9b8f7b 70%,#5c7a3c)}
.listing h4{margin:20px 10px 2px;font-weight:400;font-size:17px}
.listing .sub{margin:0 10px;font-size:13px;color:#555;padding-bottom:10px;border-bottom:1px solid var(--line)}
.listing .price-row{margin:18px 10px 0;display:flex;justify-content:space-between;align-items:center}
.tag{background:var(--teal);color:var(--white);font-size:13px;padding:6px 12px}
.price{color:var(--teal);font-size:23px;font-weight:600}
.specs{margin:16px 10px 0;padding-top:12px;border-top:1px solid var(--line);display:flex;justify-content:space-between;font-size:13px;color:#444}
.form{padding:14px}
.field{border:1px solid #ccc;height:44px;margin-bottom:14px;font-size:15px;color:#aaa;padding:10px 16px}
.field.msg{height:94px}
.submit{display:inline-block;background:var(--teal);color:var(--white);font-family:'Cinzel',Georgia,serif;font-weight:700;font-size:20px;padding:8px 26px}
.review{padding:28px 18px}
.review .who{display:flex;align-items:center;gap:12px}
.avatar{width:120px;height:120px;border-radius:50%;border:2px solid #ccc;background:radial-gradient(circle at 50% 45%,#c99a82,#5b3b2a)}
.review .name{font-family:'Cinzel',Georgia,serif;color:var(--teal);font-size:18px}
.review .role{font-family:'Cinzel',Georgia,serif;font-size:18px;color:#222}
.review blockquote{margin-top:26px;font-style:italic;font-size:12.5px;line-height:20px;color:#333}
.review blockquote::before{content:"\201C";font-size:34px;color:#bbb;vertical-align:-10px;margin-right:4px}
.review blockquote::after{content:"\201D";font-size:34px;color:#bbb;vertical-align:-16px;margin-left:4px}

.footer{height:363px;background:linear-gradient(180deg,#27303a,#1a1f25);position:relative;color:var(--white)}
.fcol{position:absolute;top:64px}
.fcol h5{font-family:'Cinzel',Georgia,serif;font-weight:400;font-size:21px;margin-bottom:24px}
.fcol h5 em{font-style:normal;color:var(--lime)}
.links li{list-style:none;font-size:14px;margin-bottom:20px}
.links li::before{content:"\203A";margin-right:10px}
.crow{display:flex;gap:14px;font-size:15px;margin-bottom:32px;align-items:flex-start}
.crow .sq{width:33px;height:33px;background:var(--lime);flex:none;display:flex;align-items:center;justify-content:center}
.srow{display:flex;align-items:center;gap:18px;font-size:12px;text-transform:uppercase;margin-bottom:16px}
.srow i{width:38px;height:38px;border-radius:50%;display:block}
.fbrand{position:absolute;left:846px;top:160px;font-family:'Cinzel',Georgia,serif;font-weight:700;font-size:38px;color:#9a9a9a;line-height:1.05}
.fbrand small{display:block;font-size:27px;letter-spacing:2px}
.copy{height:45px;background:var(--teal);color:var(--white);font-size:14px;display:flex;align-items:center;justify-content:center}
</style>
</head>
<body>

<div class="topbar">
  <div class="contact">
    <span><svg width="13" height="13" viewBox="0 0 24 24"><path fill="#fff" d="M6.6 10.8a15 15 0 0 0 6.6 6.6l2.2-2.2c.3-.3.7-.4 1-.2 1.1.4 2.3.6 3.6.6.6 0 1 .4 1 1V20c0 .6-.4 1-1 1A17 17 0 0 1 3 4c0-.6.4-1 1-1h3.5c.6 0 1 .4 1 1 0 1.3.2 2.5.6 3.6.1.3 0 .7-.2 1z"/></svg>555-014-2290</span>
    <span><svg width="14" height="11" viewBox="0 0 24 18"><path fill="#fff" d="M0 0h24v18H0z"/><path fill="none" stroke="#0ea88e" stroke-width="2" d="M1 1l11 9 11-9"/></svg>info@norvalerealestate.com</span>
  </div>
  <div class="social"><i></i><i></i><i></i><i></i></div>
</div>

<header class="header">
  <div class="brand">Norvale<small>Real Estate</small></div>
  <div class="cta">Schedule Free Consultation</div>
  <nav class="nav">
    <a href="#">Find a Home</a><a href="#">Sell Your Home</a><a href="#">Norvale Blog</a><a href="#">Our Agents</a><a href="#">Contact Us</a>
  </nav>
</header>

<section class="hero" role="img" aria-label="City skyline of downtown high-rise towers under a blue sky">
  <span class="arrow prev"><svg width="10" height="12" viewBox="0 0 10 12"><path d="M7 1 2 6l5 5" fill="none" stroke="#222" stroke-width="2"/></svg></span>
  <span class="arrow next"><svg width="10" height="12" viewBox="0 0 10 12"><path d="M3 1l5 5-5 5" fill="none" stroke="#fff" stroke-width="2"/></svg></span>
  <div class="caption">Lanterly Homes Collective Offers Assistance &amp; Expertise To Home Buyers, Sellers &amp; Investors.</div>
</section>

<section class="welcome">
  <h1>Welcome to <b>Norvale Real Estate</b></h1>
  <p class="intro">Lorem ipsum dolor sit amet, consectetuer adipiscing elit, sed diam nonummy nibh euismod tincidunt ut laoreet dolore magna aliquam erat volutpat. Ut wisi enim ad minim veniam, quis nostrud exerci tation ullamcorper suscipit lobortis nisl ut aliquip ex ea commodo consequat. Duis autem vel eum iriure dolor in hendrerit in vulputate velit esse molestie consequat, vel illum dolore eu feugiat nulla facilisis at vero</p>
  <div class="offer buy">
    <div class="photo" role="img" aria-label="Modern living room interior with sofas and a ceiling of round lights"></div>
    <h3>BUY WITH US</h3>
    <p>Lorem ipsum dolor sit amet, consectetuer adipiscing elit, sed diam nonummy nibh euismod tincidunt ut laoreet dolore magna aliquam erat volutpat. Ut wisi enim ad minim veniam,</p>
  </div>
  <div class="offer sell">
    <div class="photo" role="img" aria-label="Couple greeting an agent in front of a house"></div>
    <h3>SELL WITH US</h3>
    <p>Lorem ipsum dolor sit amet, consectetuer adipiscing elit, sed diam nonummy nibh euismod tincidunt ut laoreet dolore magna aliquam erat volutpat. Ut wisi enim ad minim veniam,</p>
  </div>
</section>

<section class="why">
  <h2>Why Choose Us</h2>
  <div class="feature" style="left:110px;top:133px">
    <div class="icon active"><svg width="50" height="50" viewBox="0 0 50 50"><circle cx="25" cy="25" r="18" fill="none" stroke="#fff" stroke-width="3"/><text x="25" y="33" text-anchor="middle" font-family="Open Sans,sans-serif" font-size="24" font-weight="700" fill="#fff">$</text></svg></div>
    <p>A Proven Brokerage</p>
  </div>
  <div class="feature" style="left:451px;top:133px">
    <div class="icon"><svg width="52" height="40" viewBox="0 0 52 40"><rect x="4" y="10" width="44" height="24" fill="none" stroke="#222" stroke-width="3"/><circle cx="26" cy="22" r="6" fill="none" stroke="#222" stroke-width="3"/><path d="M8 6h40" stroke="#222" stroke-width="3"/></svg></div>
    <p>No Junk Fees</p>
  </div>
  <div class="feature" style="left:792px;top:133px">
    <div class="icon"><svg width="50" height="44" viewBox="0 0 50 44"><rect x="4" y="4" width="42" height="28" fill="#222"/><rect x="20" y="32" width="10" height="6" fill="#222"/><rect x="13" y="38" width="24" height="3" fill="#222"/></svg></div>
    <p>Professional Marketing</p>
  </div>
  <div class="feature" style="left:110px;top:318px">
    <div class="icon"><svg width="46" height="50" viewBox="0 0 46 50"><path d="M8 4h22l8 8v34H8z" fill="none" stroke="#222" stroke-width="3"/><path d="M14 18h16M14 25h16M14 32h10" stroke="#222" stroke-width="3"/><path d="M28 40l12-14 4 4-12 14h-4z" fill="#222"/></svg></div>
    <p>Electronic Signatures</p>
  </div>
  <div class="feature" style="left:451px;top:318px">
    <div class="icon"><svg width="40" height="52" viewBox="0 0 40 52"><rect x="8" y="4" width="24" height="44" rx="4" fill="none" stroke="#222" stroke-width="3"/><circle cx="20" cy="42" r="2" fill="#222"/><path d="M12 10h16" stroke="#222" stroke-width="3"/></svg></div>
    <p>Digital Marketing Experts</p>
  </div>
  <div class="feature" style="left:792px;top:318px">
    <div class="icon"><svg width="52" height="52" viewBox="0 0 52 52"><circle cx="26" cy="26" r="6" fill="#222"/><g fill="#222"><circle cx="26" cy="7" r="4"/><circle cx="44" cy="20" r="4"/><circle cx="38" cy="42" r="4"/><circle cx="14" cy="42" r="4"/><circle cx="8" cy="20" r="4"/></g><path d="M26 26V7M26 26l18-6M26 26l12 16M26 26 14 42M26 26 8 20" stroke="#222" stroke-width="2"/></svg></div>
    <p>Our Vendor Network</p>
  </div>
</section>

<section class="panels">
  <div class="panel" style="left:80px">
    <h2>Featured Listings <span class="nav-arrows">‹ ›</span></h2><div class="rule"></div>
    <div class="card listing">
      <div class="photo" role="img" aria-label="Two-storey stone house with a front lawn"></div>
      <h4>123 Dollar Smit Amet</h4>
      <p class="sub">Duis autem vel eum iriure</p>
      <div class="price-row"><span class="tag">For Rent</span><span class="price">$ 123, 000</span></div>
      <div class="specs"><span>1200 sq ft</span><span>2 Beds</span><span>2 Baths</span></div>
    </div>
  </div>
  <div class="panel" style="left:438px">
    <h2>Quick Inquiry</h2><div class="rule"></div>
    <div class="card form">
      <div class="field">Your name</div>
      <div class="field">Your email</div>
      <div class="field">Your phone number</div>
      <div class="field msg">Your message</div>
      <span class="submit">Submit</span>
    </div>
  </div>
  <div class="panel" style="left:794px">
    <h2>Customer Reviews <span class="nav-arrows">‹ ›</span></h2><div class="rule"></div>
    <div class="card review">
      <div class="who">
        <div class="avatar" role="img" aria-label="Portrait photo of the reviewer"></div>
        <div><div class="name">Mara Ellison</div><div class="role">Designation</div></div>
      </div>
      <blockquote>Lorem ipsum dolor sit amet, consece dipiscing elit, sed dianonummy nibh euismod tincid ut laoreet dolore magna aliquam erat dipiscing elit, anonummy erat dipiscing elit, sed dianonummy nibh euismod nibh euismod tincidunt ut laoreet dolore m aliquam erat dipiscing elit, sed dianonummy nibh euismod volutpat. Utwisi enim ad minim.</blockquote>
    </div>
  </div>
</section>

<footer class="footer" role="contentinfo">
  <div class="fcol" style="left:82px">
    <h5>Quick <em>Links</em></h5>
    <ul class="links"><li>Find A Home</li><li>Sell Your Home</li><li>Norvale Blog</li><li>Our Agents</li><li>Contact Us</li></ul>
  </div>
  <div class="fcol" style="left:301px">
    <h5>Contact <em>Details</em></h5>
    <div class="crow"><span class="sq"><svg width="14" height="18" viewBox="0 0 14 18"><path d="M7 0a7 7 0 0 1 7 7c0 5-7 11-7 11S0 12 0 7a7 7 0 0 1 7-7z" fill="#fff"/><circle cx="7" cy="7" r="2.5" fill="#8cc63f"/></svg></span><span><b>Office:</b><br>123. Lorem ipsum dolor<br>sit amet, consecte 32145</span></div>
    <div class="crow"><span class="sq"><svg width="16" height="16" viewBox="0 0 24 24"><path fill="#fff" d="M6.6 10.8a15 15 0 0 0 6.6 6.6l2.2-2.2c.3-.3.7-.4 1-.2 1.1.4 2.3.6 3.6.6.6 0 1 .4 1 1V20c0 .6-.4 1-1 1A17 17 0 0 1 3 4c0-.6.4-1 1-1h3.5c.6 0 1 .4 1 1 0 1.3.2 2.5.6 3.6.1.3 0 .7-.2 1z"/></svg></span><span style="padding-top:6px">555 014 2290</span></div>
    <div class="crow"><span class="sq"><svg width="18" height="13" viewBox="0 0 24 18"><path fill="#fff" d="M0 0h24v18H0z"/><path fill="none" stroke="#8cc63f" stroke-width="2" d="M1 1l11 9 11-9"/></svg></span><span style="padding-top:6px">info@norvalerealestate.com</span></div>
  </div>
  <div class="fcol" style="left:629px">
    <h5>Follow <em>Us</em></h5>
    <div class="srow"><i style="background:#1f5fa8"></i>Social One</div>
    <div class="srow"><i style="background:#1aa3d9"></i>Social Two</div>
    <div class="srow"><i style="background:#1580b9"></i>Social Three</div>
    <div class="srow"><i style="background:#d6402c"></i>Social Four</div>
  </div>
  <div class="fbrand">Norvale<small>Real Estate</small></div>
</footer>
<div class="copy">Copyright © 2016 Norvale Real Estate. All rights reserved.</div>

</body>
</html>
```